A design led business card for the construction industry

High-end business card to match logo. White logo on dark grey/off black to the front. Matching dark font on white to back, possibly with logo design again.

We offer construction and project management services to commercial and private clients in the UK. Projetcs range from newbuilds, conversion of listed buildings and refurbishments and extensions of existing homes. Our focus is on quality and attention to detail using the highest skills.

Contact Information for Business Card

Name; Dylan Marsh BSc
Position; Project Manager
Mobile; 07961 284 657
Tel; 01632 845192
email; dylan@craftvale.co.uk
web; www.craftvale.co.uk
Address; Oakford on Wey, KT4 7PX

Colors

Designer to choose only greyscale colors for use in the design.

Requirements
Must have
• To include the below description of the business,

CONSTRUCTION - PROJECT MANAGEMENT
Nice to have
• The posibility of the top back of the card being used as a ruler. So will have a measurement to scale in mm or an architect scale of 1:50
Should not have
• Should not be portrait

```html
<!DOCTYPE html>
<html lang="en">
<head>
<meta charset="utf-8">
<title>Craftvale – Business Card</title>
<link href="https://fonts.googleapis.com/css2?family=Roboto:wght@400;500&display=swap" rel="stylesheet">
<style>
  :root {
    --stage: #e4e4e4;
    --card-dark: #2b2b2b;
    --card-dark-ink: #474747;
    --card-light: #f4f4f4;
    --ink: #262626;
    --rule: #8a8a8a;
  }
  * { margin: 0; padding: 0; box-sizing: border-box; }
  html, body { width: 1200px; height: 960px; overflow: hidden; }
  body {
    position: relative;
    background: var(--stage);
    font-family: "Roboto", Arial, sans-serif;
    color: var(--ink);
  }
  .card {
    position: absolute;
    left: 328px;
    width: 544px;
    height: 350px;
  }
  .card--front { top: 110px; background: var(--card-dark); }
  .card--back  { top: 503px; background: var(--card-light); }

  .front-wordmark {
    position: absolute;
    left: 0; right: 0;
    top: 150px;
    text-align: center;
    font-size: 34px;
    font-weight: 400;
    letter-spacing: 14px;
    padding-left: 14px;
    color: var(--card-dark-ink);
  }

  .scale-ruler { position: absolute; left: 0; top: 0; width: 544px; height: 40px; }
  .scale-ruler text { font-family: "Roboto", Arial, sans-serif; font-size: 10px; fill: var(--ink); }

  .back-wordmark {
    position: absolute;
    left: 40px;
    top: 162px;
    width: 212px;
    text-align: center;
    font-size: 24px;
    font-weight: 400;
    letter-spacing: 7px;
    padding-left: 7px;
    color: var(--ink);
  }

  .divider {
    position: absolute;
    left: 271px;
    top: 97px;
    width: 2px;
    height: 157px;
    background: var(--rule);
  }

  .contact {
    position: absolute;
    left: 297px;
    top: 96px;
    font-size: 15.5px;
    line-height: 19px;
  }
  .contact__name { font-size: 18.5px; font-weight: 500; line-height: 22px; }
  .contact__role { margin-bottom: 17px; }
  .contact__address { margin-bottom: 6px; }
  .contact__line { display: flex; align-items: center; gap: 5px; }
  .contact__line svg { width: 13px; height: 13px; flex: none; }

  .tagline {
    position: absolute;
    left: 0; right: 0;
    top: 300px;
    text-align: center;
    font-size: 15.5px;
    letter-spacing: 0.1px;
  }
</style>
</head>
<body>

<section class="card card--front">
  <div class="front-wordmark">CRAFTVALE</div>
</section>

<section class="card card--back">
  <svg class="scale-ruler" viewBox="0 0 544 40" aria-label="1:50 scale ruler">
    <defs>
      <pattern id="minor-ticks" patternUnits="userSpaceOnUse" x="33" y="0" width="12.8" height="16">
        <rect x="0" y="0" width="1" height="16" fill="#262626"/>
      </pattern>
    </defs>
    <rect x="33" y="0" width="500" height="16" fill="url(#minor-ticks)"/>
    <g fill="#262626">
      <rect x="97"  y="0" width="1" height="25"/>
      <rect x="225" y="0" width="1" height="25"/>
      <rect x="353" y="0" width="1" height="25"/>
      <rect x="481" y="0" width="1" height="25"/>
      <rect x="33"  y="0" width="1" height="37"/>
      <rect x="161" y="0" width="1" height="37"/>
      <rect x="289" y="0" width="1" height="37"/>
      <rect x="417" y="0" width="1" height="37"/>
    </g>
    <text x="7" y="37">1:50</text>
    <text x="166" y="37">1m</text>
    <text x="294" y="37">2m</text>
    <text x="422" y="37">3m</text>
  </svg>

  <div class="back-wordmark">CRAFTVALE</div>

  <div class="divider"></div>

  <div class="contact">
    <p class="contact__name">Dylan Marsh BSc</p>
    <p class="contact__role">Project Manager</p>
    <p class="contact__address">Oakford on Wey, KT4 7PX</p>
    <p class="contact__line">
      <svg viewBox="0 0 13 13" aria-hidden="true"><rect x="3.5" y="0.8" width="6" height="11.4" rx="1" fill="none" stroke="#262626" stroke-width="1.2"/><rect x="5.5" y="10" width="2" height="1" fill="#262626"/></svg>
      07961 284 657
    </p>
    <p class="contact__line">
      <svg viewBox="0 0 13 13" aria-hidden="true"><path d="M2.6 1 L4.8 1 L5.6 3.8 L4.3 5 Q5.5 7.6 8 8.7 L9.2 7.4 L12 8.2 L12 10.4 Q11.6 12 10 12 Q1 11.2 1 2.6 Q1 1 2.6 1 Z" fill="#262626"/></svg>
      01632 845192
    </p>
    <p class="contact__line">
      <svg viewBox="0 0 13 13" aria-hidden="true"><rect x="0.8" y="2.8" width="11.4" height="7.6" fill="none" stroke="#262626" stroke-width="1.1"/><path d="M0.8 2.8 L6.5 7.4 L12.2 2.8 M0.8 10.4 L5 6.2 M12.2 10.4 L8 6.2" fill="none" stroke="#262626" stroke-width="1"/></svg>
      dylan@craftvale.co.uk
    </p>
    <p class="contact__line">
      <svg viewBox="0 0 13 13" aria-hidden="true"><g fill="none" stroke="#262626" stroke-width="0.9"><circle cx="6.5" cy="6.5" r="5.6"/><ellipse cx="6.5" cy="6.5" rx="2.5" ry="5.6"/><path d="M0.9 6.5 H12.1 M1.8 3.6 H11.2 M1.8 9.4 H11.2"/></g></svg>
      www.craftvale.co.uk
    </p>
  </div>

  <p class="tagline">CONSTRUCTION - PROJECT MANAGEMENT</p>
</section>

</body>
</html>
```